Rivex Management LLC Business Card

The sample logo was attached for the business Card Design for Traffic Control Company named Rivex Management LLC. Card design needs to have the company logo and colors match the logo color. It will be nice to show some images of Traffic control signs or cones, even roads closer that math the company services

Target Market(s)

Temporary traffic control. Road closer.

Industry/Entity Type

Construction

Contact Information for Business Card

basic information, name, job title, address, email phone, website

Font styles to use
Serif
Sans Serif

Colors
F0912C
F2A743
F7CA91
FBE8D2
FDF5EE
EE7325
F08F49
F5BC92
FAE3D3
FDF4ED

```html
<!DOCTYPE html>
<html lang="en">
<head>
<meta charset="utf-8">
<title>Rivex Management LLC Business Card</title>
<link href="https://fonts.googleapis.com/css2?family=Montserrat:wght@500;600;700&family=Roboto:wght@400;500&display=swap" rel="stylesheet">
<style>
  :root {
    --orange: #EE7325;
    --orange-soft: #F08F49;
    --charcoal: #4b4b4b;
    --ink: #2f2f2f;
    --rule: #6d6d6d;
    --paper: #ffffff;
    --backdrop: #bdbdbd;
    --sign-yellow: #F5CB1A;
  }
  * { box-sizing: border-box; margin: 0; padding: 0; }
  html, body { width: 1200px; height: 788px; overflow: hidden; }
  body {
    background: var(--backdrop);
    display: flex;
    align-items: center;
    justify-content: center;
    gap: 48px;
    font-family: "Roboto", Arial, sans-serif;
  }
  .card {
    position: relative;
    width: 540px;
    height: 309px;
    border-bottom: 5px solid var(--orange);
    box-shadow: 0 10px 24px rgba(0,0,0,.25);
    overflow: hidden;
  }
  .card--front { background: var(--paper); }
  .card--back { background: var(--charcoal); }

  .brand-name {
    font-family: "Montserrat", Arial, sans-serif;
    font-weight: 700;
    letter-spacing: .04em;
    text-transform: uppercase;
    line-height: 1.15;
  }
  .card--front .brand {
    position: absolute;
    left: 34px;
    top: 0;
    bottom: 0;
    width: 200px;
    display: flex;
    align-items: center;
    gap: 12px;
  }
  .brand-mark {
    flex: none;
    width: 18px;
    height: 18px;
    background: var(--orange);
  }
  .card--front .brand-name { color: var(--orange); font-size: 24px; }

  .divider {
    position: absolute;
    left: 262px;
    top: 58px;
    width: 2px;
    height: 190px;
    background: linear-gradient(var(--rule) 0 22%, var(--orange) 22% 78%, var(--rule) 78% 100%);
  }

  .contact {
    position: absolute;
    left: 288px;
    top: 62px;
    right: 20px;
    color: var(--ink);
    font-size: 12.5px;
    line-height: 1.55;
  }
  .contact__name {
    font-family: "Montserrat", Arial, sans-serif;
    font-weight: 700;
    font-size: 22px;
    color: var(--orange);
    text-transform: uppercase;
    line-height: 1.1;
  }
  .contact__title { margin-bottom: 12px; }
  .contact__address { margin-bottom: 10px; }
  .contact__line { display: flex; align-items: center; gap: 8px; }
  .contact__line svg { width: 11px; height: 11px; flex: none; fill: var(--orange); }

  .card--back .brand {
    position: absolute;
    top: 52px;
    left: 0;
    right: 0;
    display: flex;
    justify-content: center;
    align-items: center;
    gap: 14px;
  }
  .card--back .brand-name { color: #ffffff; font-size: 32px; }

  .sign-row {
    position: absolute;
    left: 50px;
    right: 50px;
    bottom: 46px;
    height: 92px;
    background: var(--sign-yellow);
    border-radius: 6px;
  }
</style>
</head>
<body>
  <section class="card card--front">
    <div class="brand">
      <span class="brand-mark"></span>
      <span class="brand-name">Rivex Management LLC</span>
    </div>
    <div class="divider"></div>
    <div class="contact">
      <p class="contact__name">Daniel Reyes</p>
      <p class="contact__title">CEO/Founder</p>
      <p class="contact__address">Suite 5, 24 Country Name<br>Street Name ABC 4579</p>
      <p class="contact__line">
        <svg viewBox="0 0 24 24"><path d="M6.6 10.8a15.1 15.1 0 0 0 6.6 6.6l2.2-2.2c.3-.3.7-.4 1-.2 1.1.4 2.3.6 3.6.6.6 0 1 .4 1 1V20c0 .6-.4 1-1 1A17 17 0 0 1 3 4c0-.6.4-1 1-1h3.5c.6 0 1 .4 1 1 0 1.3.2 2.5.6 3.6.1.3 0 .7-.2 1z"/></svg>
        (555) 018 2746
      </p>
      <p class="contact__line">
        <svg viewBox="0 0 24 24"><path d="M2 5h20v14H2zm2 2v.5l8 5 8-5V7zm0 2.8V17h16V9.8l-8 5z"/></svg>
        info@rivexmanagementllc.com
      </p>
      <p class="contact__line">
        <svg viewBox="0 0 24 24"><circle cx="12" cy="12" r="10"/></svg>
        www.rivexmanagementllc.com
      </p>
    </div>
  </section>

  <section class="card card--back">
    <div class="brand">
      <span class="brand-mark"></span>
      <span class="brand-name">Rivex Management LLC</span>
    </div>
    <div class="sign-row" role="img" aria-label="Row of five yellow diamond road warning signs showing curve and lane-merge arrows"></div>
  </section>
</body>
</html>
```